Hacienda Valle Dorado Business cards

We would like 3 individual business cards with the logo you designed:

1) Marta Pellworth - Phone: 360 555 0147
2) Theodore K Pellworth - Phone 206 555 0183
3) Dana Whitlow - Phone 310-555-0126

Address for all three cards:
4217 288th Ave NE
Elkhorn Bend, WA 98019
HaciendaValleDorado@mailbox-example.com

```html
<!DOCTYPE html>
<html lang="en">
<head>
<meta charset="utf-8">
<title>Hacienda Valle Dorado — Business Card</title>
<link rel="stylesheet" href="https://fonts.googleapis.com/css2?family=Roboto:wght@400;700&display=swap">
<style>
  :root {
    --backdrop: #161719;
    --card: #26282b;
    --card-edge: #f2f2f2;
    --ink: #e9e9ea;
    --ink-soft: #cfd0d2;
    --icon-fill: #ececec;
    --icon-mark: #26282b;
  }
  * { margin: 0; padding: 0; box-sizing: border-box; }
  html, body {
    width: 1200px;
    height: 900px;
    overflow: hidden;
    background: var(--backdrop);
    font-family: "Roboto", Arial, sans-serif;
  }
  .canvas {
    width: 1200px;
    height: 900px;
    display: flex;
    align-items: center;
    justify-content: center;
  }
  .business-card {
    position: relative;
    width: 980px;
    height: 560px;
    background: var(--card);
    border-bottom: 6px solid var(--card-edge);
    color: var(--ink);
    display: flex;
    flex-direction: column;
    align-items: center;
  }
  .brand {
    margin-top: 110px;
    display: flex;
    flex-direction: column;
    align-items: center;
    gap: 22px;
  }
  .brand-dot {
    width: 28px;
    height: 28px;
    border-radius: 50%;
    background: var(--ink);
  }
  .brand-name {
    font-weight: 400;
    font-size: 42px;
    letter-spacing: 4px;
    text-transform: uppercase;
    color: var(--ink);
  }
  .holder-name {
    margin-top: 44px;
    font-weight: 700;
    font-size: 24px;
    letter-spacing: 2px;
    text-transform: uppercase;
    color: var(--ink);
  }
  .contact {
    position: absolute;
    left: 70px;
    right: 70px;
    bottom: 56px;
    display: grid;
    grid-template-columns: auto auto;
    justify-content: space-between;
    row-gap: 18px;
    align-items: center;
  }
  .contact-item {
    display: flex;
    align-items: center;
    gap: 12px;
    font-size: 22px;
    color: var(--ink-soft);
  }
  .contact-icon { width: 32px; height: 32px; flex: none; }
  .address {
    grid-column: 1 / -1;
    font-weight: 700;
    font-size: 22px;
    color: var(--ink);
    padding-left: 44px;
  }
</style>
</head>
<body>
<main class="canvas">
  <article class="business-card">
    <header class="brand">
      <span class="brand-dot"></span>
      <h1 class="brand-name">Hacienda Valle Dorado</h1>
    </header>

    <p class="holder-name">Marta Pellworth</p>

    <section class="contact">
      <p class="contact-item phone">
        <svg class="contact-icon" viewBox="0 0 32 32" aria-hidden="true">
          <circle cx="16" cy="16" r="16" fill="var(--icon-fill)"/>
          <path d="M11 8.5c.8-.6 1.8-.4 2.3.4l1.5 2.6c.4.7.2 1.6-.4 2.1l-1 .8c.9 2 2.4 3.6 4.3 4.6l.9-1c.5-.6 1.4-.8 2.1-.4l2.6 1.5c.8.5 1 1.6.4 2.3l-1 1.3c-.7.9-1.9 1.2-3 .8-4.6-1.7-8-5.2-9.6-9.9-.4-1.1 0-2.3.9-3z" fill="var(--icon-mark)"/>
        </svg>
        360 555 0147
      </p>
      <p class="contact-item email">
        <svg class="contact-icon" viewBox="0 0 32 32" aria-hidden="true">
          <circle cx="16" cy="16" r="16" fill="var(--icon-fill)"/>
          <rect x="8" y="10.5" width="16" height="11" rx="1.2" fill="var(--icon-mark)"/>
          <path d="M8.6 11.2 16 17l7.4-5.8" fill="none" stroke="var(--icon-fill)" stroke-width="1.4"/>
        </svg>
        HaciendaValleDorado@mailbox-example.com
      </p>
      <p class="address">4217 288th Ave NE Elkhorn Bend, WA 98019</p>
    </section>
  </article>
</main>
</body>
</html>
```